Halvorsen Partners Business Card

Halvorsen Partners Civil Construction
Marcus Halvorsen
CEO
727-518-6094
Marcus@HalvorsenSiteworks.example
www.HalvorsenSiteworks.example
Site Development
Utility Construction
Excavation
40876 County Lane 19
Land O' Lakes, FL 34638

Target Market(s)

Construction and government

Industry/Entity Type

Business

Contact Information for Business Card

I want an unique design that make a statement

Number of Pages Required

1 page

Font styles to use

Colors

Designer to choose colors to be used in the design.

Requirements
Must have
• unique design, feel free to modify or change the color of my logo.
Nice to have
• extra design features like spot UV, foil accents, color edges, unique paper, or any thing that would make my card pop.
• I like the feel of the image that I attached

```html
<!DOCTYPE html>
<html lang="en">
<head>
<meta charset="utf-8">
<title>Halvorsen Partners Business Card</title>
<link href="https://fonts.googleapis.com/css2?family=Open+Sans:wght@400;600;700&family=Open+Sans+Condensed:wght@700&display=swap" rel="stylesheet">
<style>
  :root {
    --brand-blue: #2553a8;
    --brand-blue-deep: #1b3f8f;
    --brand-blue-light: #2f63bf;
    --paper: #f7f7f7;
    --steel: #9a9ca0;
    --ink-grey: #6d6f73;
    --stage: #e8e5e0;
    --white: #ffffff;
  }
  * { margin: 0; padding: 0; box-sizing: border-box; }
  html, body { width: 1200px; height: 780px; overflow: hidden; }
  body {
    background: var(--stage);
    font-family: "Open Sans", Arial, sans-serif;
    position: relative;
  }
  .card {
    position: absolute;
    top: 235px;
    width: 540px;
    height: 309px;
    border-radius: 4px;
    overflow: hidden;
    box-shadow: 0 10px 28px rgba(0,0,0,0.18);
  }
  .card-front { left: 40px; background: var(--paper); }
  .card-back {
    left: 620px;
    background: radial-gradient(ellipse at 60% 35%, var(--brand-blue-light) 0%, var(--brand-blue) 55%, var(--brand-blue-deep) 100%);
  }
  .front-swoosh { position: absolute; inset: 0; }

  .brand-lockup {
    position: absolute;
    display: flex;
    align-items: center;
    gap: 14px;
  }
  .brand-square { width: 40px; height: 40px; background: var(--brand-blue); }
  .brand-divider { width: 1px; height: 50px; background: var(--steel); }
  .brand-name {
    font-family: "Open Sans Condensed", "Open Sans", Arial, sans-serif;
    font-weight: 700;
    font-size: 27px;
    line-height: 1;
    letter-spacing: 0.5px;
    text-transform: uppercase;
    white-space: nowrap;
  }
  .brand-tagline {
    margin-top: 6px;
    font-size: 11.5px;
    letter-spacing: 5px;
    text-transform: uppercase;
    white-space: nowrap;
  }

  .card-front .brand-lockup { left: 40px; top: 70px; }
  .card-front .brand-name { color: var(--brand-blue); }
  .card-front .brand-tagline { color: var(--ink-grey); }

  .person { position: absolute; left: 40px; top: 150px; }
  .person-name {
    font-size: 17px; font-weight: 600; color: var(--brand-blue);
    text-transform: uppercase; letter-spacing: 0.3px;
    white-space: nowrap; line-height: 1.3;
  }
  .person-title { font-size: 12px; color: var(--ink-grey); margin-top: 1px; }

  .contact-list {
    position: absolute; left: 40px; top: 208px;
    list-style: none;
  }
  .contact-item {
    display: flex; align-items: center; gap: 8px;
    font-size: 12px; color: var(--ink-grey);
    height: 22px;
    white-space: nowrap;
  }
  .contact-icon { width: 15px; height: 15px; flex: none; }

  .card-back .brand-lockup { left: 110px; top: 100px; }
  .card-back .brand-square { background: var(--white); }
  .card-back .brand-divider { background: rgba(255,255,255,0.6); }
  .card-back .brand-name, .card-back .brand-tagline { color: var(--white); }

  .service-line {
    position: absolute; left: 0; right: 0; top: 212px;
    text-align: center;
    font-size: 13px; color: var(--white); letter-spacing: 0.2px;
  }
</style>
</head>
<body>

<section class="card card-front" aria-label="Business card front">
  <svg class="front-swoosh" viewBox="0 0 540 309" preserveAspectRatio="none" aria-hidden="true">
    <defs>
      <linearGradient id="frontBlue" x1="0" y1="0" x2="1" y2="1">
        <stop offset="0" stop-color="#2f63bf"/>
        <stop offset="1" stop-color="#1b3f8f"/>
      </linearGradient>
    </defs>
    <path d="M380 0 H540 V309 H430 C520 220 520 70 380 0 Z" fill="url(#frontBlue)"/>
    <path d="M350 0 C505 60 520 215 418 309" fill="none" stroke="#9a9ca0" stroke-width="5"/>
  </svg>

  <div class="brand-lockup">
    <div class="brand-square"></div>
    <div class="brand-divider"></div>
    <div>
      <div class="brand-name">Halvorsen Partners</div>
      <div class="brand-tagline">Civil Construction</div>
    </div>
  </div>

  <div class="person">
    <div class="person-name">Marcus Halvorsen</div>
    <div class="person-title">CEO</div>
  </div>

  <ul class="contact-list">
    <li class="contact-item">
      <svg class="contact-icon" viewBox="0 0 16 16" aria-hidden="true"><rect width="16" height="16" rx="2" fill="#2553a8"/><path d="M5 3.5l2 2-1 1.2c.7 1.4 1.7 2.4 3.1 3.1l1.2-1 2 2-1.2 1.5C7.8 11.8 4.2 8.2 3.7 4.7z" fill="#fff"/></svg>
      727-518-6094
    </li>
    <li class="contact-item">
      <svg class="contact-icon" viewBox="0 0 16 16" aria-hidden="true"><rect width="16" height="16" rx="2" fill="#2553a8"/><rect x="3" y="4.5" width="10" height="7" fill="none" stroke="#fff" stroke-width="1.2"/><path d="M3 4.5l5 4 5-4" fill="none" stroke="#fff" stroke-width="1.2"/></svg>
      Marcus@HalvorsenSiteworks.example
    </li>
    <li class="contact-item">
      <svg class="contact-icon" viewBox="0 0 16 16" aria-hidden="true"><rect width="16" height="16" rx="2" fill="#2553a8"/><circle cx="8" cy="8" r="5" fill="none" stroke="#fff" stroke-width="1.1"/><ellipse cx="8" cy="8" rx="2.2" ry="5" fill="none" stroke="#fff" stroke-width="1"/><path d="M3 8h10" stroke="#fff" stroke-width="1"/></svg>
      www.HalvorsenSiteworks.example
    </li>
  </ul>
</section>

<section class="card card-back" aria-label="Business card back">
  <div class="brand-lockup">
    <div class="brand-square"></div>
    <div class="brand-divider"></div>
    <div>
      <div class="brand-name">Halvorsen Partners</div>
      <div class="brand-tagline">Civil Construction</div>
    </div>
  </div>
  <p class="service-line">Site Development | Utility Construction | Excavation</p>
</section>

</body>
</html>
```